new business card and logo for a high end Automotive repair and performance shop

Need to update our design for our business cards. New address, and want a new look. I'll upload some pics of our current card. We are a high end auto repair/tuning shop. New address will be 5192 W. Larkfield Ave BROOKVALE, T.X. 75990. I do have the vector files if needed. The logo would have a similar design. Love the look of carbon fiber, and brushed aluminum, although may have issues showing the texture of the material due to dpi restrictions during card printing. Also the logo would have to be easily printed on shirts, and for embroidery. Thanks, and good luck.

www.motor-zenith.example

Target Market(s)

High end automotive repair, dealership alternative.

Industry/Entity Type

Automotive

Contact Information for Business Card

MOTORZENITH
5192 W. LARKFIELD AVE
BROOKVALE, T.X. 75990
PH 555-307-9261
FAX 555-307-4470
EMAIL INFO@MOTOR-ZENITH.EXAMPLE

Logo Text

MotorZenith

Font styles to use
Sans Serif

Requirements
Must have
• name, address, description that was uploaded.
Nice to have
• maybe some brands i.e. vardo, orvex, Talvani, qrt, solvanta, dovik etc. not necessary. simple is good, like the look of carbon fiber, brushed aluminum.
Should not have
• open to all suggestions.

```html
<!DOCTYPE html>
<html lang="en">
<head>
<meta charset="utf-8">
<title>MotorZenith Business Card</title>
<link rel="stylesheet" href="https://fonts.googleapis.com/css2?family=Bodoni+Moda:wght@500&family=Raleway:wght@500;700&display=swap">
<style>
  :root {
    --canvas-bg: #eeeeee;
    --card-dark: #0b0b0b;
    --card-mid: #2a2a2a;
    --accent-red: #8e0f10;
    --mark-red: #5a0a0b;
    --text-red: #c4161c;
    --text-white: #f4f4f4;
    --silver: #c9cbcd;
  }
  html, body {
    margin: 0;
    padding: 0;
    width: 1200px;
    height: 901px;
    overflow: hidden;
    background: var(--canvas-bg);
  }
  .canvas {
    position: relative;
    width: 1200px;
    height: 901px;
  }
  .card {
    position: absolute;
    width: 470px;
    height: 268px;
    overflow: hidden;
    background: radial-gradient(ellipse at 55% 50%, var(--card-mid) 0%, #151515 45%, var(--card-dark) 100%);
    box-shadow: 0 8px 18px rgba(0,0,0,0.35);
  }
  .card--front { left: 200px; top: 225px; }
  .card--back  { left: 505px; top: 480px; }
  .card__bands {
    position: absolute;
    inset: 0;
    width: 100%;
    height: 100%;
  }
  .band { fill: var(--accent-red); }

  .brand {
    position: absolute;
    left: 0;
    right: 0;
    top: 114px;
    display: flex;
    align-items: center;
    justify-content: center;
    gap: 12px;
  }
  .brand__dot {
    width: 16px;
    height: 16px;
    border-radius: 50%;
    background: var(--silver);
  }
  .brand__name {
    font-family: "Raleway", sans-serif;
    font-weight: 700;
    font-size: 30px;
    letter-spacing: 1px;
    color: var(--silver);
  }

  .brand-mark-small {
    position: absolute;
    right: 46px;
    top: 50px;
    font-family: "Raleway", sans-serif;
    font-weight: 700;
    font-size: 13px;
    color: var(--mark-red);
  }

  .contact {
    position: absolute;
    left: 30px;
    right: 20px;
    top: 82px;
    text-align: center;
    font-family: "Raleway", sans-serif;
  }
  .contact__name {
    margin: 0;
    font-family: "Bodoni Moda", serif;
    font-weight: 500;
    font-size: 34px;
    letter-spacing: 3px;
    color: var(--text-white);
    text-transform: uppercase;
    line-height: 1;
  }
  .contact__title {
    margin: 5px 0 3px;
    font-size: 12px;
    letter-spacing: 8px;
    color: var(--text-red);
    text-transform: uppercase;
  }
  .contact__line {
    margin: 0;
    font-size: 10.5px;
    font-weight: 500;
    letter-spacing: 0.8px;
    line-height: 1.4;
    color: var(--text-white);
    text-transform: uppercase;
    white-space: nowrap;
  }
  .contact__accent { color: var(--text-red); }
</style>
</head>
<body>
<main class="canvas">

  <section class="card card--front" aria-label="Business card front">
    <svg class="card__bands" viewBox="0 0 470 268" aria-hidden="true">
      <polygon class="band" points="362,0 470,0 470,40 420,74 250,74"/>
      <polygon class="band" points="0,202 206,202 93,268 0,268"/>
    </svg>
    <div class="brand">
      <span class="brand__dot"></span>
      <span class="brand__name">MotorZenith</span>
    </div>
  </section>

  <section class="card card--back" aria-label="Business card back">
    <svg class="card__bands" viewBox="0 0 470 268" aria-hidden="true">
      <polygon class="band" points="362,0 470,0 470,40 420,74 250,74"/>
      <polygon class="band" points="0,202 206,202 93,268 0,268"/>
    </svg>
    <span class="brand-mark-small">MotorZenith</span>
    <div class="contact">
      <h1 class="contact__name">Dorian Pell</h1>
      <p class="contact__title">Owner</p>
      <p class="contact__line"><span class="contact__accent">MOTORZENITH</span>, 5192 W. Larkfield Ave</p>
      <p class="contact__line">Brookvale, T.X. 75990 · PH 555-307-9261</p>
      <p class="contact__line">FAX 555-307-4470 · <span class="contact__accent">Email INFO@MOTOR-ZENITH.EXAMPLE</span></p>
    </div>
  </section>

</main>
</body>
</html>
```